Defend science flier

Put my name and text below on one side of flier, and place other text on other side. Try to keep file about 4 by 6 or 6 by 8 inches.

Target Market(s)

Community and retailers.

Industry/Entity Type

Retail and concerned community.

Font styles to use
Serif

Requirements
Must have
• Good, eye-catching titles. Be smaller format. Not 8 by 11
Nice to have
• Black and white text. Maybe bullets etc for organizion but no decorations.
Should not have
• Any decoration

```html
<!DOCTYPE html>
<html lang="en">
<head>
<meta charset="utf-8">
<title>Martin Keller, Ph.D. – Flier Sizes</title>
<link href="https://fonts.googleapis.com/css2?family=Figtree:wght@300;400;500;600;700&display=swap" rel="stylesheet">
<style>
  :root {
    --board: #808080;
    --label: #f2f2f2;
    --cream: #fbf8ee;
    --white: #ffffff;
    --ink: #111111;
    --ink-soft: #2a2a2a;
    --gold: #a88c4f;
    --gold-line: #b39a62;
    --photo-dark: #24170f;
    --photo-mid: #5a3d24;
    --photo-light: #c9a267;
  }
  * { box-sizing: border-box; margin: 0; padding: 0; }
  html, body { width: 923px; height: 1200px; overflow: hidden; }
  body {
    background: var(--board);
    font-family: "Figtree", "Helvetica Neue", Arial, sans-serif;
    color: var(--ink);
    position: relative;
  }
  .size-label {
    position: absolute;
    width: 300px;
    text-align: center;
    font-weight: 300;
    font-size: 23px;
    color: var(--label);
    letter-spacing: 0.3px;
  }
  .card {
    position: absolute;
    background: var(--cream);
    overflow: hidden;
    text-align: center;
  }
  .card > * { position: absolute; left: 0; right: 0; }

  /* ---------- shared pieces ---------- */
  .flier-name { font-weight: 700; letter-spacing: -0.3px; line-height: 1; }
  .flier-tagline { font-weight: 500; line-height: 1; }
  .hero-photo {
    background:
      radial-gradient(ellipse 45% 55% at 47% 62%, var(--photo-light) 0%, var(--photo-mid) 45%, transparent 75%),
      linear-gradient(90deg, var(--photo-dark), #3a2818 50%, var(--photo-dark));
  }
  .intro p { font-weight: 400; color: var(--ink-soft); }
  .quote-box {
    background: var(--white);
    border: 1px solid var(--gold-line);
    border-radius: 5px;
  }
  .quote-text { font-weight: 700; color: var(--ink); }
  .quote-credit { font-weight: 400; color: var(--ink-soft); }
  .site-footer {
    background: var(--gold);
    color: var(--white);
  }
  .site-footer strong { display: block; font-weight: 600; letter-spacing: 0.2px; }
  .site-footer span { display: block; font-weight: 400; }

  .sins-box {
    background: var(--white);
    border: 1px solid var(--gold-line);
    border-radius: 5px;
    text-align: left;
  }
  .sins-title { font-weight: 700; text-align: center; }
  .sins-intro { font-weight: 600; }
  .sins-list { list-style: none; counter-reset: sin; }
  .sins-list li {
    counter-increment: sin;
    position: absolute;
    font-weight: 600;
    display: flex;
    align-items: center;
  }
  .sins-list li::before {
    content: counter(sin);
    flex: none;
    border-radius: 50%;
    background: var(--gold);
    color: var(--white);
    box-shadow: inset 0 0 0 2px var(--gold), inset 0 0 0 3.5px var(--white);
    display: flex;
    align-items: center;
    justify-content: center;
    font-weight: 500;
  }
  .commentary p { font-weight: 400; color: var(--ink-soft); }

  /* ---------- 6x8 ---------- */
  .card--lg { width: 408px; height: 543px; top: 100px; }
  .card--lg.front { left: 28px; }
  .card--lg.back { left: 486px; }
  .card--lg .flier-name { top: 15px; font-size: 27px; }
  .card--lg .flier-tagline { top: 53px; font-size: 14px; }
  .card--lg .hero-photo { top: 80px; height: 159px; }
  .card--lg .intro { top: 252px; padding: 0; }
  .card--lg .intro p { font-size: 11.8px; line-height: 14.8px; margin-bottom: 7.5px; white-space: nowrap; }
  .card--lg .quote-box { top: 369px; left: 22px; right: 22px; height: 118px; padding: 10px 12px 0; }
  .card--lg .quote-text { font-size: 9.6px; line-height: 12.4px; }
  .card--lg .quote-credit { font-size: 9.8px; line-height: 13.2px; margin-top: 7px; }
  .card--lg .site-footer { top: 496px; height: 47px; padding-top: 7px; }
  .card--lg .site-footer strong { font-size: 12.2px; line-height: 15px; }
  .card--lg .site-footer span { font-size: 12.2px; line-height: 16px; }

  .card--lg .sins-box { top: 21px; left: 22px; right: 22px; height: 276px; }
  .card--lg .sins-title { position: absolute; top: 16px; left: 0; right: 0; font-size: 16.5px; }
  .card--lg .sins-intro { position: absolute; top: 45px; left: 38px; right: 30px; font-size: 13px; line-height: 16px; }
  .card--lg .sins-list li { left: 35px; right: 20px; font-size: 12.2px; line-height: 14.8px; height: 28px; }
  .card--lg .sins-list li::before { width: 27px; height: 27px; margin-right: 8px; font-size: 19px; }
  .card--lg .sins-list li:nth-child(1) { top: 82px; }
  .card--lg .sins-list li:nth-child(2) { top: 118px; }
  .card--lg .sins-list li:nth-child(3) { top: 154px; }
  .card--lg .sins-list li:nth-child(4) { top: 190px; }
  .card--lg .sins-list li:nth-child(5) { top: 227px; }
  .card--lg .commentary { top: 314px; padding: 0 24px; }
  .card--lg .commentary p { font-size: 12.2px; line-height: 14.7px; margin-bottom: 14.5px; }

  /* ---------- 4x6 ---------- */
  .card--sm { width: 272px; height: 408px; top: 745px; }
  .card--sm.front { left: 96px; }
  .card--sm.back { left: 554px; }
  .card--sm .flier-name { top: 15px; font-size: 18.5px; }
  .card--sm .flier-tagline { top: 40px; font-size: 9.6px; }
  .card--sm .hero-photo { top: 59px; height: 100px; }
  .card--sm .intro { top: 168px; padding: 0 20px; }
  .card--sm .intro p { font-size: 8px; line-height: 10.3px; margin-bottom: 10px; }
  .card--sm .quote-box { top: 261px; left: 17px; right: 17px; height: 105px; padding: 7px 7px 0; }
  .card--sm .quote-text { font-size: 7.8px; line-height: 10.2px; }
  .card--sm .quote-credit { font-size: 7.8px; line-height: 9.8px; margin-top: 6px; }
  .card--sm .site-footer { top: 373px; height: 35px; padding-top: 6px; }
  .card--sm .site-footer strong { font-size: 8.6px; line-height: 11px; }
  .card--sm .site-footer span { font-size: 8.6px; line-height: 11px; }

  .card--sm .sins-box { top: 17px; left: 17px; right: 17px; height: 196px; }
  .card--sm .sins-title { position: absolute; top: 8px; left: 0; right: 0; font-size: 12px; }
  .card--sm .sins-intro { position: absolute; top: 29px; left: 15px; right: 12px; font-size: 8.6px; line-height: 11.5px; }
  .card--sm .sins-list li { left: 12px; right: 8px; font-size: 7.9px; line-height: 10.6px; height: 20px; }
  .card--sm .sins-list li::before { width: 19px; height: 19px; margin-right: 6px; font-size: 13px; box-shadow: inset 0 0 0 1.5px var(--gold), inset 0 0 0 2.6px var(--white); }
  .card--sm .sins-list li:nth-child(1) { top: 56px; }
  .card--sm .sins-list li:nth-child(2) { top: 82px; }
  .card--sm .sins-list li:nth-child(3) { top: 108px; }
  .card--sm .sins-list li:nth-child(4) { top: 134px; }
  .card--sm .sins-list li:nth-child(5) { top: 160px; }
  .card--sm .commentary { top: 226px; padding: 0 18px; }
  .card--sm .commentary p { font-size: 8.2px; line-height: 10.7px; margin-bottom: 10px; }
</style>
</head>
<body>

  <div class="size-label" style="left:82px; top:38px;">6x8 Front</div>
  <div class="size-label" style="left:540px; top:38px;">6x8 Back</div>
  <div class="size-label" style="left:82px; top:696px;">4x6 Front</div>
  <div class="size-label" style="left:540px; top:696px;">4x6 Back</div>

  <section class="card card--lg front">
    <h1 class="flier-name">Martin Keller, Ph.D.</h1>
    <p class="flier-tagline">“The Halvorsen and Brightwater of Psychology and History.”</p>
    <div class="hero-photo" role="img" aria-label="Photo of an open old book glowing in warm light in front of a shelf of leather-bound volumes"></div>
    <div class="intro">
      <p>Martin’s Bio-Psych has Restructured the Liberal Arts and Sciences—<br>from Genetics to the Fine Arts and Hollywood.</p>
      <p>Museum Catalogues, Better Nonfiction, and Hollywood Films<br>Now Use Martin’s Methods.</p>
      <p>Martin’s Biopsych is endorsed by Dr. Harold Winfield, professor of<br>psychiatry at Easton Medical School, who said:</p>
    </div>
    <blockquote class="quote-box">
      <p class="quote-text">“Modern sleep and dream research teaches us—as does Martin Keller’s book Human Fault or Social Fault—that all human activities, including art and politics, are products of the human brain, and that each of us has the privilege and responsibility of using it and communicating its creations.”</p>
      <p class="quote-credit">—Dr. Harold Winfield, Professor of Psychiatry, Emeritus, Easton Medical School, author of ‘Night Minds: An Introduction to Sleep Science’ (Redmond University Press, 2004).</p>
    </blockquote>
    <footer class="site-footer"><strong>SEE MARTIN’S HOMEPAGE FOR MORE DETAILS:</strong><span>www.martin-keller.org</span></footer>
  </section>

  <section class="card card--lg back">
    <div class="sins-box">
      <h2 class="sins-title">Why Did the Culture Change?</h2>
      <p class="sins-intro">During the 1960s, we socialized the Seven Deadly Sins. Therefore:</p>
      <ol class="sins-list">
        <li>Pride became “Racism.”</li>
        <li>Lust became “Sexism” and “Gender“ existing “out there.”</li>
        <li>Gluttony became “Consumer Fetishism.”</li>
        <li>Vanity became “Media Images of Beauty.”</li>
        <li>Sloth became The lack of social action: “Are you fighting for diversity?”</li>
      </ol>
    </div>
    <div class="commentary">
      <p>This “fight for diversity” inspires attacks against people like Dr. Keller for asserting any reality principle about human nature.</p>
      <p>These thugs are religious crusaders who ignore the rule of law and try to stop the progress of science. These fanatics go around and give people a “tear-test”—as during the Salem witch trials. Don’t let them take over.</p>
      <p>The educational and culture elites—such as Hollywood—now reject these theological “social sins.” The elites are replacing theology with traditional, human-based sin.</p>
    </div>
    <footer class="site-footer"><strong>SEE MARTIN’S HOMEPAGE FOR MORE DETAILS:</strong><span>www.martin-keller.org</span></footer>
  </section>

  <section class="card card--sm front">
    <h1 class="flier-name">Martin Keller, Ph.D.</h1>
    <p class="flier-tagline">“The Halvorsen and Brightwater of Psychology and History.”</p>
    <div class="hero-photo" role="img" aria-label="Photo of an open old book glowing in warm light in front of a shelf of leather-bound volumes"></div>
    <div class="intro">
      <p>Martin’s Bio-Psych has Restructured the Liberal Arts and Sciences— from Genetics to the Fine Arts and Hollywood.</p>
      <p>Museum Catalogues, Better Nonfiction, and Hollywood Films Now Use Martin’s Methods.</p>
      <p>Martin’s Biopsych is endorsed by Dr. Harold Winfield, professor of psychiatry at Easton Medical School, who said:</p>
    </div>
    <blockquote class="quote-box">
      <p class="quote-text">“Modern sleep and dream research teaches us—as does Martin Keller’s book Human Fault or Social Fault—that all human activities, including art and politics, are products of the human brain, and that each of us has the privilege and responsibility of using it and communicating its creations.”</p>
      <p class="quote-credit">—Dr. Harold Winfield, Professor of Psychiatry, Emeritus, Easton Medical School, author of ‘Night Minds: An Introduction to Sleep Science’ (Redmond University Press, 2004).</p>
    </blockquote>
    <footer class="site-footer"><strong>SEE MARTIN’S HOMEPAGE FOR MORE DETAILS:</strong><span>www.martin-keller.org</span></footer>
  </section>

  <section class="card card--sm back">
    <div class="sins-box">
      <h2 class="sins-title">Why Did the Culture Change?</h2>
      <p class="sins-intro">During the 1960s, we socialized the Seven Deadly Sins. Therefore:</p>
      <ol class="sins-list">
        <li>Pride became “Racism.”</li>
        <li>Lust became “Sexism” and “Gender“ existing “out there.”</li>
        <li>Gluttony became “Consumer Fetishism.”</li>
        <li>Vanity became “Media Images of Beauty.”</li>
        <li>Sloth became The lack of social action: “Are you fighting for diversity?”</li>
      </ol>
    </div>
    <div class="commentary">
      <p>This “fight for diversity” inspires attacks against people like Dr. Keller for asserting any reality principle about human nature.</p>
      <p>These thugs are religious crusaders who ignore the rule of law and try to stop the progress of science. These fanatics go around and give people a “tear-test”—as during the Salem witch trials. Don’t let them take over.</p>
      <p>The educational and culture elites—such as Hollywood—now reject these theological “social sins.” The elites are replacing theology with traditional, human-based sin.</p>
    </div>
    <footer class="site-footer"><strong>SEE MARTIN’S HOMEPAGE FOR MORE DETAILS:</strong><span>www.martin-keller.org</span></footer>
  </section>

</body>
</html>
```